PACKAGING Pistacho Ice cream cup 500 ml

Ice cream PACKAGING round cup design

packing design for supermarkets displays

Focus in a premium new upmarket ice cream brand whit traditional ingredients and artisan traditionals flavors

1.- must be in : CMYK
2.- design in Photoshop CS6 or adobe illustrator CS6
3.- design must be in layers by element (name, picture , flavor, nutritiom fact, etc)
4.- 600 dpi resolution

Target Market(s)

upmarket ice cream consumers

Industry/Entity Type

Food Production

Colors
000000
474747
abd036
9bcb3c
fece3e

Requirements
Must have
• importatn highlights
• 5.-Text : HELADO PREMIUM
• 6.- Cup background : black dluxe
• 7.- Banner flavor text : PISTACHO
• 8.- Banner flavor color : Green whit lights efects and golden border lines
• 9.- Text : 500 ml
• 10.- picture : like ball icecream whit natural pistachos decoration.
• 11.- cup background waterbase waves
• 12 .- rectangle area 6cm width by 9cm high for nutritional information, ingredients and legal information

```html
<!DOCTYPE html>
<html lang="es">
<head>
<meta charset="utf-8">
<title>Helado Premium Pistacho – etiqueta de vaso 500 ml</title>
<link rel="stylesheet" href="https://fonts.googleapis.com/css2?family=Marcellus&family=Cinzel:wght@700&display=swap">
<style>
  :root {
    --canvas: #ffffff;
    --deluxe-black: #050606;
    --panel-white: #ffffff;
    --gold-light: #e9d6a8;
    --gold-mid: #b8925a;
    --bronze: #6b3b22;
    --pistachio: #abd036;
    --pistachio-light: #c6e05a;
    --pistachio-dark: #9bcb3c;
    --cream: #f3d2b6;
    --yellow: #fece3e;
    --ink: #1a1410;
  }
  * { box-sizing: border-box; margin: 0; padding: 0; }
  html, body { width: 1200px; height: 1200px; overflow: hidden; background: var(--canvas); }
  .canvas { position: relative; width: 1200px; height: 1200px; }

  .cup-wrap {
    position: absolute; left: 0; top: 373px; width: 1200px; height: 454px;
    background: radial-gradient(ellipse at 50% 50%, #121414 0%, var(--deluxe-black) 70%);
  }

  .info-panel {
    position: absolute; top: 21px; width: 276px; height: 410px;
    border-radius: 14px; padding: 5px;
    background: linear-gradient(90deg, var(--bronze), var(--gold-light) 50%, var(--bronze));
  }
  .info-panel::after {
    content: ""; position: absolute; inset: 5px; border-radius: 10px;
    background: var(--panel-white);
  }
  .info-panel--left { left: 40px; }
  .info-panel--right { left: 882px; }

  .gold-rules { position: absolute; left: 0; top: 0; }

  .hero-photo {
    position: absolute; left: 484px; top: 216px; width: 316px; height: 212px;
    border-radius: 45% 45% 40% 40%;
    background: radial-gradient(ellipse at 50% 45%, #efe6d4 0%, #9c7bb8 35%, #6a3a2a 65%, rgba(5,6,6,0) 80%);
    z-index: 1;
  }

  .brand-seal {
    position: absolute; left: 568px; top: 37px; width: 116px; height: 116px;
    border-radius: 50%; background: var(--deluxe-black);
    border: 3px solid var(--bronze);
    display: flex; flex-direction: column; align-items: center; justify-content: center; gap: 6px;
    z-index: 3;
  }
  .brand-seal__dot { width: 34px; height: 34px; border-radius: 50%; background: var(--cream); }
  .brand-seal__name {
    font-family: "Marcellus", serif; font-size: 11px; line-height: 1.1;
    color: var(--cream); text-align: center; letter-spacing: 0.5px;
  }

  .title-plate {
    position: absolute; left: 420px; top: 143px; width: 414px; height: 70px;
    border: 3px solid var(--bronze); border-radius: 18px;
    box-shadow: inset 0 0 0 1px var(--gold-mid);
    background: var(--deluxe-black);
    display: flex; align-items: center; justify-content: center;
    z-index: 2;
  }
  .title-plate__text {
    font-family: "Marcellus", serif; font-size: 42px; line-height: 1; color: var(--pistachio);
    letter-spacing: -0.5px; white-space: nowrap;
  }

  .volume {
    position: absolute; left: 345px; top: 251px;
    font-family: "Marcellus", serif; font-size: 18px; color: var(--yellow);
  }

  .flavor-banner { position: absolute; left: 400px; top: 300px; z-index: 3; }
  .flavor-banner__text {
    font-family: "Cinzel", serif; font-weight: 700; font-size: 50px; fill: var(--ink);
  }
</style>
</head>
<body>
<main class="canvas">
  <section class="cup-wrap">
    <svg class="gold-rules" width="1200" height="454" viewBox="0 0 1200 454" aria-hidden="true">
      <defs>
        <linearGradient id="goldRule" x1="0" x2="1">
          <stop offset="0" stop-color="#6b3b22"/>
          <stop offset="0.5" stop-color="#e9d6a8"/>
          <stop offset="1" stop-color="#6b3b22"/>
        </linearGradient>
      </defs>
      <rect x="316" y="64" width="566" height="4" fill="url(#goldRule)"/>
      <rect x="316" y="91" width="566" height="4" fill="url(#goldRule)"/>
      <rect x="316" y="119" width="566" height="4" fill="url(#goldRule)"/>
      <rect x="316" y="419" width="566" height="3" fill="url(#goldRule)"/>
    </svg>

    <div class="info-panel info-panel--left" aria-label="Información nutricional, ingredientes y datos legales"></div>
    <div class="info-panel info-panel--right" aria-label="Información nutricional, ingredientes y datos legales"></div>

    <div class="hero-photo" role="img" aria-label="Fotografía de bolas de helado con frutos rojos y hojas de menta"></div>

    <div class="brand-seal">
      <span class="brand-seal__dot"></span>
      <span class="brand-seal__name">NEVADA<br>HELADOS</span>
    </div>

    <div class="title-plate"><span class="title-plate__text">HELADO PREMIUM</span></div>

    <p class="volume">500ml</p>

    <svg class="flavor-banner" width="430" height="150" viewBox="0 0 430 150">
      <defs>
        <linearGradient id="ribbonGreen" x1="0" y1="0" x2="0" y2="1">
          <stop offset="0" stop-color="#c6e05a"/>
          <stop offset="0.5" stop-color="#abd036"/>
          <stop offset="1" stop-color="#9bcb3c"/>
        </linearGradient>
      </defs>
      <polygon points="8,88 46,74 52,132 12,140" fill="#7f9d25" stroke="#b8925a" stroke-width="2"/>
      <polygon points="388,20 420,48 424,118 392,92" fill="#7f9d25" stroke="#b8925a" stroke-width="2"/>
      <polygon points="42,136 380,90 388,16 34,66" fill="url(#ribbonGreen)" stroke="#b8925a" stroke-width="3"/>
      <text class="flavor-banner__text" x="212" y="100" text-anchor="middle" transform="rotate(-8 212 80)">PISTACHO</text>
    </svg>
  </section>
</main>
</body>
</html>
```